Bright and beautiful business card for a coach

I'm a personal and business coach based in Perth, Australia. I need a business card that whilst subtle and elegant, will stand out and appeal on a table full of cards.

My business name is Tide Mentoring and the business card must represent the warmth and brightness implied in the name, without being gimmicky. It must have a warmth and appeal and be easy to read.

I prefer clean, minimalist designs.

It must align with the feel of my website and socials: https://www.tidementoring.com.au/
https://www.instagram.com/tidementoringau/
https://www.facebook.com/tidementoringau
Updates

Hi Designers Thank you so much for taking the time to submit designs. I wonder if I could have explained myself a little better. Most of the designs that have been submitted look rather formal and many have quite corporate looking embellishments on them (to my eye). I would like softer, warmer, more organic. I’m open to people playing about and being more abstract, using softer embellishments (e.g the line drawing flowers and grasses I’ve used in my socials) incorporating other colours from my palette or like the social icons in my email signature (in PDF), perhaps playing with size/oversize, playing with the bleed. Please don’t be constrained by what I’ve already done, it merely needs to compliment. I’m sorry if I’m not using the right words or have led you astray. I’m no designer, but I’ve done my website, socials, email signature etc all myself (my logo was a design contest) and I was really hoping for my business card to be something more creative than I could have made with a template. Reminder: No black cards/sides please. Thank you 😊

Target Market(s)

Individuals, most likely but not all female. Creative thinkers. Likely professionals.

Industry/Entity Type

Business & Personal Coach

Contact Information for Business Card

(Tide Mentoring Logo) Name: Maren Delsby; Title: Business & Personal Coach; Phone number: +61 (0)438 915307; Email: maren@tidementoring.com.au; Website: https://tidementoring.com.au; Social icons for Facebook, Instagram & LinkedIn: @tidementoringAU. Optional strapline: "A thinking partner to help you cut through the noise"

Font styles to use
Sans Serif

Colors
00AB8E
00BBA5
67D7C9
C6EFE9
E9F9F6
59FF00
82FF00
B8FF75
E3FFCB
F4FFEA
FFC000
F8CF3A
FAE287
FDF2CF
FEFAEE

Requirements
Must have
• Must align with feel of my website and socials. Must have a pop of #FFC000 (possibly whole of one side, or at least a block). Bright or white background. Easy to read.
Nice to have
• Possibly incorporate the sunshine/grass picture I have used in website and socials - will upload.
Should not have
• Must not be black or dark. Not impersonal or corporate looking.

```html
<!DOCTYPE html>
<html lang="en">
<head>
<meta charset="utf-8">
<title>Tide Mentoring — Business Card</title>
<link href="https://fonts.googleapis.com/css2?family=Lato:wght@300;400&display=swap" rel="stylesheet">
<style>
  :root {
    --page-bg: #ecebe7;
    --card-bg: #ffffff;
    --amber-deep: #c67c2c;
    --amber: #e9a02c;
    --gold: #ffc000;
    --sun: #f8c22a;
    --lime-haze: #c9c94a;
    --wave-yellow: #e3c93a;
    --text-dark: #4a4a4a;
    --text-mid: #666666;
    --text-soft: #a9a9a9;
    --icon-gold: #f3b817;
    --icon-mint: #a9d8c8;
    --white: #ffffff;
  }
  * { margin: 0; padding: 0; box-sizing: border-box; }
  html, body {
    width: 1200px; height: 900px; overflow: hidden;
    background: var(--page-bg);
    font-family: "Lato", "Helvetica Neue", Arial, sans-serif;
  }
  .card {
    position: absolute; left: 75px; top: 150px;
    width: 1050px; height: 600px;
    background: var(--card-bg);
    overflow: hidden;
  }
  .card-art { position: absolute; inset: 0; }
  .brand {
    position: absolute; left: 56px; top: 118px;
    display: flex; align-items: center; gap: 16px;
    color: var(--white); font-weight: 300; font-size: 56px; letter-spacing: 1px;
    white-space: nowrap;
  }
  .brand-dot {
    width: 30px; height: 30px; border-radius: 50%;
    border: 2px solid var(--white);
  }
  .tagline {
    position: absolute; right: 64px; top: 112px;
    text-align: right; color: var(--white);
    font-size: 31px; font-weight: 400; line-height: 40px; letter-spacing: .3px;
  }
  .portrait {
    position: absolute; left: 287px; top: 347px;
    width: 114px; height: 114px; border-radius: 50%;
    background: radial-gradient(circle at 50% 45%, #c8a08a, #6f5a4c 75%);
  }
  .person { position: absolute; right: 650px; top: 474px; text-align: right; white-space: nowrap; }
  .person-name { font-size: 41px; font-weight: 300; color: var(--text-dark); line-height: 48px; }
  .person-title { font-size: 28px; font-weight: 300; color: var(--text-soft); line-height: 34px; }
  .contact {
    position: absolute; right: 118px; white-space: nowrap;
    font-weight: 300; color: var(--text-mid); text-align: right;
  }
  .contact-phone { top: 332px; font-size: 34px; font-weight: 400; color: var(--text-dark); }
  .contact-email { top: 384px; font-size: 31px; }
  .contact-web { top: 455px; font-size: 31px; }
  .contact-social { top: 511px; font-size: 31px; right: 190px; }
  .icon {
    position: absolute; width: 32px; height: 32px; border-radius: 50%;
    background: var(--icon-gold);
    display: flex; align-items: center; justify-content: center;
    color: var(--white); font-size: 20px; font-weight: 400;
  }
  .icon-social { background: var(--icon-mint); width: 30px; height: 30px; }
</style>
</head>
<body>
  <div class="card">
    <svg class="card-art" viewBox="0 0 1050 600" width="1050" height="600">
      <defs>
        <linearGradient id="band-fill" x1="0" y1="0" x2="1" y2="0">
          <stop offset="0" stop-color="#c9812e"/>
          <stop offset="0.35" stop-color="#c98530"/>
          <stop offset="0.62" stop-color="#f0ad2a"/>
          <stop offset="0.8" stop-color="#f9c12a"/>
          <stop offset="1" stop-color="#c5c84a"/>
        </linearGradient>
        <radialGradient id="band-glow" cx="0.78" cy="0.15" r="0.35">
          <stop offset="0" stop-color="#fbd23a" stop-opacity=".8"/>
          <stop offset="1" stop-color="#fbd23a" stop-opacity="0"/>
        </radialGradient>
        <linearGradient id="wave-fill" x1="0" y1="0" x2="1" y2="0">
          <stop offset="0" stop-color="#d8c838"/>
          <stop offset="0.45" stop-color="#f2c12a"/>
          <stop offset="1" stop-color="#e8a22a"/>
        </linearGradient>
      </defs>
      <path class="wave-accent" fill="url(#wave-fill)"
        d="M0 300 C14 330 18 395 40 422 C68 452 112 432 152 408 C245 348 330 274 470 270 H1050 V275 H470 C335 280 245 340 150 400 C92 436 48 432 30 398 C18 372 12 332 0 312 Z"/>
      <g role="img" aria-label="Sunlit grass meadow photograph in warm amber and golden tones">
        <path fill="url(#band-fill)"
          d="M0 0 H1050 V270 H470 C330 274 240 335 140 395 C85 428 45 425 30 392 C18 362 12 322 0 302 Z"/>
        <path fill="url(#band-glow)"
          d="M0 0 H1050 V270 H470 C330 274 240 335 140 395 C85 428 45 425 30 392 C18 362 12 322 0 302 Z"/>
      </g>
    </svg>

    <div class="brand"><span class="brand-dot"></span>Tide Mentoring</div>

    <p class="tagline">A thinking<br>partner to help<br>you cut through the noise</p>

    <div class="portrait" role="img" aria-label="Portrait photo of Maren Delsby"></div>

    <div class="person">
      <p class="person-name">Maren Delsby</p>
      <p class="person-title">Business &amp; Personal Coach</p>
    </div>

    <p class="contact contact-phone">+61 (0)438 915307</p>
    <span class="icon" style="left:954px;top:338px">
      <svg width="18" height="18" viewBox="0 0 24 24"><path fill="#fff" d="M6.6 10.8a15.1 15.1 0 0 0 6.6 6.6l2.2-2.2c.3-.3.7-.4 1-.2 1.1.4 2.3.6 3.6.6.6 0 1 .4 1 1V20c0 .6-.4 1-1 1A17 17 0 0 1 3 4c0-.6.4-1 1-1h3.5c.6 0 1 .4 1 1 0 1.3.2 2.5.6 3.6.1.3 0 .7-.2 1z"/></svg>
    </span>

    <p class="contact contact-email">maren@tidementoring.com.au</p>
    <span class="icon" style="left:954px;top:392px">@</span>

    <p class="contact contact-web">https://tidementoring.com.au</p>
    <span class="icon" style="left:954px;top:462px">
      <svg width="18" height="18" viewBox="0 0 24 24" fill="none" stroke="#fff" stroke-width="2.4" stroke-linecap="round"><path d="M10 14a4 4 0 0 0 5.6 0l3-3a4 4 0 0 0-5.6-5.6l-1 1"/><path d="M14 10a4 4 0 0 0-5.6 0l-3 3a4 4 0 0 0 5.6 5.6l1-1"/></svg>
    </span>

    <p class="contact contact-social">@tidementoringAU</p>
    <span class="icon icon-social" style="left:884px;top:516px"></span>
    <span class="icon icon-social" style="left:920px;top:516px"></span>
    <span class="icon icon-social" style="left:955px;top:516px"></span>
  </div>
</body>
</html>
```